Law Firm Ad

We need a magazine/auction program design for a Sacramento based law firm. Current need is for a school auction sponsorship. Ad must be 5 1/2 x 8 1/2 in high resolution (300 dpi) and in JPG or PDF format. A clean, modern, simple design is preferred.

Thornby Law Corporation provides general preventative employment advice to employers in avoiding litigation and has counseled businesses on cases involving employment law, unfair business practices and trade secrets. Thornby Law Corporation also practices in business, real estate and employment litigation.

Target Market(s)

This particular ad it is to support Haskeldale Elementary School's 21st Annual Auction and Dinner on March 14, 2015.
Here's the facebook link https://www.examplesocial.test/HaskeldaleAuction/photos/a.918273645012398.275103.610294857361042/3049182736450192/?type=1&theater
But I would like something that might be fairly universal.

Industry/Entity Type

Real Estate

Font styles to use
Sans Serif

Requirements
Must have
• Clean and crisp design. Not overly traditional.
Nice to have
• Contact information:
Thornby Law Corporation
318 Brimley Avenue, Suite 200
Sacramento, CA 95000
916.555.0142
thornby-law.test

```html
<!DOCTYPE html>
<html lang="en">
<head>
<meta charset="utf-8">
<title>Thornby Law Firm Magazine Ad_02</title>
<link rel="stylesheet" href="https://fonts.googleapis.com/css2?family=Arimo:wght@400;700&family=Caladea&display=swap">
<style>
  :root {
    --page: #ffffff;
    --ink: #1e1e1e;
    --muted: #8a8a8a;
    --brand-orange: #e0922f;
    --frame: #b8b8b8;
    --photo-light: #c9c9c9;
    --photo-mid: #9a9a9a;
    --photo-dark: #5e5e5e;
  }
  * { margin: 0; padding: 0; box-sizing: border-box; }
  html, body {
    width: 1200px; height: 1000px; overflow: hidden;
    background: var(--page);
  }
  .sheet { position: relative; width: 1200px; height: 1000px; }
  .sheet-title {
    position: absolute; top: 66px; left: 0; width: 1200px;
    text-align: center;
    font-family: "Caladea", Georgia, serif;
    font-size: 21px; color: #000;
  }
  .ad {
    position: absolute; left: 328px; top: 110px;
    width: 545px; height: 843px;
    background: var(--page);
    border: 1px solid var(--frame);
    box-shadow: 3px 4px 5px rgba(0,0,0,0.28);
    font-family: "Arimo", Helvetica, Arial, sans-serif;
    overflow: hidden;
  }
  .ad-brand {
    position: absolute; right: 48px; top: 48px;
    font-size: 22px; font-weight: 700;
    color: var(--brand-orange);
    text-align: right; line-height: 1.1;
  }
  .ad-photo {
    position: absolute; left: 0; top: 120px;
    width: 545px; height: 363px;
    background:
      linear-gradient(180deg, var(--photo-light) 0%, var(--photo-mid) 55%, var(--photo-dark) 100%);
  }
  .ad-headline {
    position: absolute; left: 49px; top: 515px; width: 470px;
    font-size: 28.5px; font-weight: 400; line-height: 36px;
    color: var(--brand-orange);
  }
  .ad-contact {
    position: absolute; left: 49px; top: 656px;
    font-size: 12.5px; line-height: 16.3px; color: var(--ink);
    font-style: normal;
  }
  .ad-web {
    position: absolute; left: 49px; top: 739px;
    font-size: 12.5px; font-weight: 700; color: var(--ink);
  }
  .ad-copyright {
    position: absolute; left: 49px; top: 771px;
    font-size: 9.5px; color: var(--muted);
  }
  .ad-footer-band {
    position: absolute; left: 0; bottom: 0;
    width: 545px; height: 25px;
    background: var(--brand-orange);
  }
</style>
</head>
<body>
<main class="sheet">
  <h1 class="sheet-title">Thornby Law Firm Magazine Ad_02</h1>
  <section class="ad">
    <div class="ad-brand">Thornby<br>Law Corporation</div>
    <div class="ad-photo" role="img" aria-label="Black and white photo of a cheering crowd with many hands raised in the air"></div>
    <p class="ad-headline">We are proud to support Haskeldale Elementary School’s 21st Annual Auction &amp; Dinner</p>
    <address class="ad-contact">
      Thornby Law Corporation<br>
      318 Brimley Avenue, Suite 200<br>
      Sacramento, CA 95000<br>
      916.555.0142
    </address>
    <p class="ad-web">thornby-law.test</p>
    <p class="ad-copyright">© 2015 Thornby Law Corporation. All rights reserved.</p>
    <div class="ad-footer-band"></div>
  </section>
</main>
</body>
</html>
```